Business Card Design

Motorvane Ledger is an online automotive resource on a national scale specifically targeting lease purchases for new cars. Our Online and app platform allow prospective lease clients to scan a window sticker while at a franchise dealership and instantly receive a lease quote at what we call the sweet spot. Motorvane Ledger offers price transparency during the lease process to allow average people the confidence in the lease process and takes away any fear of the big franchise dealers.
Motorvane ledger allows ordinary lease customers to know they are getting a low price lease and not overpaying. Never overpay again

Industry/Entity Type

Automotive

Contact Information for Business Card

Motorvane Ledger
Martin Sowerby (President of operations)
Phone: 888-247-6031
Cell: 561-384-2706

```html
<!DOCTYPE html>
<html lang="en">
<head>
<meta charset="utf-8">
<title>Motorvane Ledger – Business Card</title>
<link rel="stylesheet" href="https://fonts.googleapis.com/css2?family=Exo+2:wght@400;500;800&display=swap">
<style>
  :root {
    --page: #e6e4e1;
    --card-white: #ffffff;
    --card-shade: #ececec;
    --ink-dark: #2f2f2f;
    --band-dark: #3a3a3a;
    --swoosh-grey: #bdbdbd;
    --swoosh-light: #dcdcdc;
    --text-light: #ffffff;
  }
  * { margin: 0; padding: 0; box-sizing: border-box; }
  html, body {
    width: 1200px; height: 901px; overflow: hidden;
    background: var(--page);
    font-family: "Exo 2", sans-serif;
  }
  .card {
    position: absolute; left: 100px; top: 165px;
    width: 1000px; height: 571px;
    border-radius: 48px; overflow: hidden;
    background: linear-gradient(180deg, var(--card-white) 0%, var(--card-shade) 60%);
    box-shadow: 0 6px 24px rgba(0,0,0,0.18);
  }
  .card-wave { position: absolute; inset: 0; width: 1000px; height: 571px; }
  .brand {
    position: absolute; left: 96px; top: 66px;
    display: flex; align-items: center; gap: 16px;
  }
  .brand-mark {
    width: 30px; height: 30px; border-radius: 50%;
    background: var(--ink-dark);
  }
  .brand-name {
    font-weight: 800; font-size: 46px; line-height: 1;
    text-transform: uppercase; letter-spacing: 0.5px;
    color: var(--ink-dark);
  }
  .holder { position: absolute; left: 100px; top: 158px; color: var(--ink-dark); }
  .holder-name { font-weight: 400; font-size: 32px; letter-spacing: 2px; text-transform: uppercase; line-height: 1.2; }
  .holder-title { font-weight: 400; font-size: 22px; margin-top: 2px; }
  .contact {
    position: absolute; right: 44px; top: 334px;
    color: var(--text-light); text-align: right;
    font-size: 20px; font-weight: 500; letter-spacing: 0.5px;
  }
  .contact-address { line-height: 1.3; margin-right: 36px; margin-bottom: 14px; }
  .contact-row {
    display: flex; justify-content: flex-end; align-items: center;
    gap: 12px; height: 29px;
  }
  .contact-row svg { width: 22px; height: 22px; fill: none; stroke: var(--text-light); stroke-width: 2; flex: none; }
</style>
</head>
<body>
  <section class="card" aria-label="Motorvane Ledger business card">
    <svg class="card-wave" viewBox="0 0 1000 571" aria-hidden="true">
      <path d="M0,262 C260,222 460,330 700,300 C850,282 950,252 1000,246 L1000,300 C940,300 850,326 700,344 C460,374 260,280 0,316 Z" fill="var(--swoosh-light)"/>
      <path d="M0,282 C260,246 460,344 700,316 C850,300 950,268 1000,262 L1000,300 C940,304 850,330 700,346 C460,370 260,284 0,314 Z" fill="var(--swoosh-grey)"/>
      <path d="M0,308 C260,272 460,356 700,330 C850,314 950,284 1000,276 L1000,571 L0,571 Z" fill="var(--band-dark)"/>
    </svg>

    <div class="brand">
      <span class="brand-mark"></span>
      <span class="brand-name">Motorvane Ledger</span>
    </div>

    <div class="holder">
      <p class="holder-name">Martin Sowerby</p>
      <p class="holder-title">Managing Director</p>
    </div>

    <div class="contact">
      <p class="contact-address">047.12th floor,Park<br>Crestline Road NVB</p>
      <div class="contact-row"><span>888-247-6031</span>
        <svg viewBox="0 0 24 24"><path d="M6 3l3 4-2 2c1 3 4 6 7 7l2-2 4 3-2 3C10 20 4 14 3 6z"/></svg></div>
      <div class="contact-row"><span>561-384-2706</span>
        <svg viewBox="0 0 24 24"><rect x="7" y="2" width="10" height="20" rx="2"/><path d="M11 18h2"/></svg></div>
      <div class="contact-row"><span>888-247-6032</span>
        <svg viewBox="0 0 24 24"><rect x="4" y="8" width="16" height="13" rx="1"/><path d="M8 8V3h8v5M8 12h2M12 12h2M8 16h2M12 16h2"/></svg></div>
      <div class="contact-row"><span>ms@motorvane.com</span>
        <svg viewBox="0 0 24 24"><rect x="3" y="6" width="18" height="12"/><path d="M3 6l9 7 9-7"/></svg></div>
      <div class="contact-row"><span>www.motorvaneledger.com</span>
        <svg viewBox="0 0 24 24"><circle cx="12" cy="12" r="9"/><path d="M3 12h18M12 3c3 3 3 15 0 18M12 3c-3 3-3 15 0 18"/></svg></div>
    </div>
  </section>
</body>
</html>
```